UK Deals and free stuff

We would like a top grade design doing which encourages users to sign up to get alerts.
The concept is that we have a database of all the best giveaways, free stuff, unbeatable deals, offers, discounts and more - similar style of deals you see on Bundlio, similar vouchers as the very best on tinsaverbook.co.uk etc.
We aggregate the best of the best UK offers and freebies and we want to build a site which the consumer has to sign up to get email alerts
The design should focus on the consumer simply entering their email, it should have a high quality padlock/security image to let them know their data is secure and that the site uses SSL encryption, it needs to state clearly we do not share their data with anyone else.
The design needs to make a big splash about the variety and type of alerts they will get in their in box and that they get the alert usually before other people on the web see it so they stand the best chance of finding the hottest deals first.
It should show the steps to signing up eg something like:
1) enter email address
2) confirm interest categories (see below)
3) click on activation link
The categories need to open out in javascript on the page (perhaps show a design with this open) which will list a set of categories (max 12) such as Electronics, Beauty, Money, All, etc
We require a logo also - domain is brightfindsnest.co.uk

```html
<!DOCTYPE html>
<html lang="en">
<head>
<meta charset="utf-8">
<title>Bright Finds Nest – Deal Alerts</title>
<link href="https://fonts.googleapis.com/css2?family=PT+Sans:wght@400;700&family=PT+Sans+Narrow:wght@400;700&display=swap" rel="stylesheet">
<style>
:root{
  --page:#e6e6e6;
  --blue:#1b6c8c;
  --brand:#1a6a96;
  --teal:#2a9fc4;
  --red:#a8191c;
  --card:#f4f4f4;
  --card-line:#d4d4d4;
  --text:#4a4a4a;
  --footer:#2c2c2c;
  --shade:rgba(40,40,40,.58);
  --chip:#eef7fb;
  --chip-line:#b9dcea;
}
*{box-sizing:border-box;margin:0;padding:0}
html,body{width:782px;height:1200px;overflow:hidden}
body{position:relative;background:var(--page);font-family:"PT Sans",Arial,sans-serif;color:var(--text)}
.abs{position:absolute}
.brand{left:118px;top:16px;font:700 24px "PT Sans Narrow",Arial,sans-serif;color:var(--brand);letter-spacing:-.3px}
.account{top:29px;height:17px;background:#2e2e2e;color:#ddd;font-size:7px;display:flex;align-items:center;justify-content:center;border-radius:2px}
.login{left:567px;width:46px}.signup{left:617px;width:47px}
.nav{left:118px;top:55px;width:546px;height:27px;background:var(--blue);display:flex;justify-content:space-around;align-items:center;font-size:6.5px;color:#dbeef5;text-transform:uppercase;border-radius:2px}
.search-label{left:137px;top:93px;font:700 17px "PT Sans Narrow",Arial,sans-serif;color:var(--brand)}
.search-btn{left:612px;top:94px;width:52px;height:18px;background:#3a3a3a;color:#ddd;font-size:7.5px;display:flex;align-items:center;justify-content:center;border-radius:2px}
.banner{left:118px;top:124px;width:546px;height:180px;background:#fafafa;border:1px solid var(--card-line)}
.banner-photo{left:4px;top:80px;width:200px;height:60px;background:linear-gradient(#d5d7da,#8f949a);border-radius:4px}
.banner-copy{right:26px;top:22px;text-align:right;font:700 24px/1.15 "PT Sans Narrow",Arial,sans-serif;color:var(--brand)}
.banner-copy .hot{color:var(--red)}
.banner-copy small{display:block;font:400 6.5px/1.5 "PT Sans",Arial,sans-serif;color:#555;margin-top:4px}
.banner-copy .partner{display:block;font:700 12px "PT Sans",Arial,sans-serif;color:#444;margin-top:10px}
.dots{right:14px;top:164px;display:flex;gap:3px}.dots i{width:7px;height:7px;border-radius:50%;background:#1f6f94}
.dots i+i{background:#999}
.section-title{left:119px;top:314px;font:400 12px "PT Sans",Arial,sans-serif;color:var(--brand);text-transform:uppercase}
.deals{left:118px;top:338px;width:546px;display:grid;grid-template-columns:repeat(4,127px);column-gap:12.5px;row-gap:16px}
.deal{height:157px;background:var(--card);border:1px solid var(--card-line);padding:10px 9px 0}
.deal-photo{height:74px;border-radius:1px}
.deal-title{margin-top:9px;font-size:8px;color:var(--teal);white-space:nowrap}
.deal-meta{font-size:6.5px;line-height:12px;color:#555;text-transform:uppercase;margin-top:3px}
.deal-buy{display:flex;align-items:center;margin-top:5px;gap:6px}
.old{font-size:10px;color:var(--red);text-decoration:line-through}
.new{font-size:10px;color:var(--red)}
.buy{margin-left:4px;background:var(--blue);color:#d6eef7;font-size:5.5px;padding:4px 7px;text-transform:uppercase;border-radius:1px}
.view-all{left:538px;top:1027px;width:125px;height:28px;background:var(--blue);color:#e2f3fa;font-size:11px;display:flex;align-items:center;justify-content:center;gap:5px;text-transform:uppercase}
.footer{left:118px;top:1066px;width:546px;height:113px;background:var(--footer);color:#bbb;padding:14px 18px}
.footer h4{font:400 9px "PT Sans",Arial,sans-serif;text-transform:uppercase;color:#ccc}
.links{position:absolute;top:31px;font-size:5px;line-height:10.5px;text-transform:uppercase;color:#aaa}
.news{position:absolute;left:301px;top:14px;width:110px}
.news p{font-size:5.5px;margin:7px 0 5px}
.news .field{height:14px;background:#555;margin-bottom:7px;font-size:5px;color:#aaa;padding:4px 6px}
.news .submit{margin-left:61px;width:50px;height:13px;background:var(--blue);font-size:5.5px;color:#cfe7f0;display:flex;align-items:center;justify-content:center}
.social{position:absolute;left:443px;top:20px;font-size:5.5px;line-height:10px;text-transform:uppercase}
.social .icons{display:flex;gap:6px;margin-top:6px}
.social .icons i{width:17px;height:17px;border-radius:50%;background:#35607f}
.social .icons i:last-child{background:#8b2424}
.social .copy{margin-top:14px;font-size:5px;line-height:9px}
.shade{inset:0;background:var(--shade)}
.modal{left:175px;top:96px;width:432px;height:308px;background:#fff;border-radius:4px;box-shadow:0 2px 10px rgba(0,0,0,.5);overflow:hidden}
.modal-head{height:46px;background:linear-gradient(#f6f6f6,#dcdcdc);display:flex;align-items:center;justify-content:center;font:700 29px "PT Sans Narrow",Arial,sans-serif;color:var(--brand);letter-spacing:-.5px}
.steps{position:absolute;top:60px;left:0;width:100%}
.step{position:absolute;width:140px;margin-left:-70px;text-align:center;color:var(--teal);font-size:11px;line-height:14px;text-transform:uppercase}
.step .num{width:58px;height:58px;margin:0 auto 8px;border-radius:50%;border:3px solid #e8e8e8;background:radial-gradient(circle at 50% 35%,#6cc8e6,#2a93bd);color:#fff;font:400 27px/52px "PT Sans Narrow",Arial,sans-serif;box-shadow:0 1px 3px rgba(0,0,0,.3)}
.categories{position:absolute;left:21px;top:166px;width:392px;background:var(--chip);border:1px solid var(--chip-line);border-radius:3px;padding:7px 8px;display:grid;grid-template-columns:repeat(4,1fr);gap:4px 6px}
.categories::before{content:"";position:absolute;left:173px;top:-6px;width:10px;height:10px;background:var(--chip);border-left:1px solid var(--chip-line);border-top:1px solid var(--chip-line);transform:rotate(45deg)}
.category{display:flex;align-items:center;gap:4px;font-size:7px;color:#3d5b68;text-transform:uppercase;height:13px}
.category .box{width:9px;height:9px;border:1px solid #8fc3d7;background:#fff;border-radius:1px;display:flex;align-items:center;justify-content:center}
.category.on .box{background:var(--teal);border-color:var(--teal)}
.rule{position:absolute;left:21px;top:243px;width:392px;border-top:1px solid #ddd}
.signup-form{position:absolute;left:25px;top:265px;width:184px;height:20px;border:1px solid #ccc;border-radius:10px;background:linear-gradient(#fff,#eee);font-size:7px;color:#666;display:flex;align-items:center;padding-left:8px}
.signup-form .go{position:absolute;right:2px;top:2px;width:28px;height:14px;border-radius:7px;background:linear-gradient(#5dc1e2,#2a8fb8);color:#fff;font-size:7px;display:flex;align-items:center;justify-content:center}
.privacy{position:absolute;left:217px;top:255px;width:205px;border-left:1px solid #ccc;padding-left:9px;display:flex;gap:7px}
.privacy svg{flex:none;margin-top:2px}
.privacy h5{font:400 7.5px "PT Sans",Arial,sans-serif;color:#333;text-transform:uppercase}
.privacy p{font-size:5px;line-height:9px;color:#555;margin-top:3px;text-transform:uppercase}
</style>
</head>
<body>
<div class="abs brand">Bright Finds Nest</div>
<div class="abs account login">LOGIN</div>
<div class="abs account signup">SIGNUP</div>
<nav class="abs nav"><span>Home</span><span>Shop by Category</span><span>Latest Deals</span><span>Popular Deals</span><span>Voucher Codes</span><span>Advanced Search</span></nav>
<div class="abs search-label">Search</div>
<div class="abs search-btn">Search</div>

<section class="abs banner">
  <div class="abs banner-photo" role="img" aria-label="Silver laptop product shot"></div>
  <div class="abs banner-copy">We Love<br><span class="hot">This Offer<br>Now !</span><small>BEST OFFER OF THE<br>WEEK IN THE INDUSTRY.</small><span class="partner">Norvik</span></div>
  <div class="abs dots"><i></i><i></i><i></i></div>
</section>

<div class="abs section-title">Latest Deals</div>

<section class="abs deals">
  <article class="deal"><div class="deal-photo" role="img" aria-label="Smartphones and tablet" style="background:linear-gradient(135deg,#ddd,#333)"></div><div class="deal-title">Half Off at Olive Branch Grocer</div><div class="deal-meta">Olive Branch Grocer<br>Maple Hollow</div><div class="deal-buy"><span class="old">$40</span><span class="new">$20</span><span class="buy">Buy this deal</span></div></article>
  <article class="deal"><div class="deal-photo" role="img" aria-label="Pizza slice" style="background:linear-gradient(135deg,#3a2418,#c4522a)"></div><div class="deal-title">Half Off at Olive Branch Grocer</div><div class="deal-meta">Olive Branch Grocer<br>Maple Hollow</div><div class="deal-buy"><span class="old">$40</span><span class="new">$20</span><span class="buy">Buy this deal</span></div></article>
  <article class="deal"><div class="deal-photo" role="img" aria-label="Row of high heel shoes" style="background:linear-gradient(90deg,#f0ece6,#c8894f,#7a3b8c,#f0ece6)"></div><div class="deal-title">Half Off at Olive Branch Grocer</div><div class="deal-meta">Olive Branch Grocer<br>Maple Hollow</div><div class="deal-buy"><span class="old">$40</span><span class="new">$20</span><span class="buy">Buy this deal</span></div></article>
  <article class="deal"><div class="deal-photo" role="img" aria-label="Wrap sandwich" style="background:linear-gradient(135deg,#c9a47a,#b9432b)"></div><div class="deal-title">Half Off at Olive Branch Grocer</div><div class="deal-meta">Olive Branch Grocer<br>Maple Hollow</div><div class="deal-buy"><span class="old">$40</span><span class="new">$20</span><span class="buy">Buy this deal</span></div></article>

  <article class="deal"><div class="deal-photo" role="img" aria-label="Denim jeans close-up" style="background:linear-gradient(135deg,#2c3f5e,#566b88)"></div><div class="deal-title">Half Off at Olive Branch Grocer</div><div class="deal-meta">Olive Branch Grocer<br>Maple Hollow</div><div class="deal-buy"><span class="old">$40</span><span class="new">$20</span><span class="buy">Buy this deal</span></div></article>
  <article class="deal"><div class="deal-photo" role="img" aria-label="Burger and fries" style="background:linear-gradient(135deg,#3b2410,#d89a3a)"></div><div class="deal-title">Half Off at Olive Branch Grocer</div><div class="deal-meta">Olive Branch Grocer<br>Maple Hollow</div><div class="deal-buy"><span class="old">$40</span><span class="new">$20</span><span class="buy">Buy this deal</span></div></article>
  <article class="deal"><div class="deal-photo" role="img" aria-label="Fashion model in fur coat" style="background:linear-gradient(135deg,#111,#6b4a35)"></div><div class="deal-title">Half Off at Olive Branch Grocer</div><div class="deal-meta">Olive Branch Grocer<br>Maple Hollow</div><div class="deal-buy"><span class="old">$40</span><span class="new">$20</span><span class="buy">Buy this deal</span></div></article>
  <article class="deal"><div class="deal-photo" role="img" aria-label="Woman eating a salad" style="background:linear-gradient(135deg,#c9d3d8,#e0b9a3)"></div><div class="deal-title">Half Off at Olive Branch Grocer</div><div class="deal-meta">Olive Branch Grocer<br>Maple Hollow</div><div class="deal-buy"><span class="old">$40</span><span class="new">$20</span><span class="buy">Buy this deal</span></div></article>

  <article class="deal"><div class="deal-photo" role="img" aria-label="Bowl of fruit" style="background:linear-gradient(135deg,#6a1f2a,#e3c34a)"></div><div class="deal-title">Half Off at Olive Branch Grocer</div><div class="deal-meta">Olive Branch Grocer<br>Maple Hollow</div><div class="deal-buy"><span class="old">$40</span><span class="new">$20</span><span class="buy">Buy this deal</span></div></article>
  <article class="deal"><div class="deal-photo" role="img" aria-label="Set of red luggage" style="background:linear-gradient(135deg,#f4f4f4,#8a1f2e)"></div><div class="deal-title">Half Off at Olive Branch Grocer</div><div class="deal-meta">Olive Branch Grocer<br>Maple Hollow</div><div class="deal-buy"><span class="old">$40</span><span class="new">$20</span><span class="buy">Buy this deal</span></div></article>
  <article class="deal"><div class="deal-photo" role="img" aria-label="Desktop computer" style="background:linear-gradient(135deg,#f6f6f6,#222)"></div><div class="deal-title">Half Off at Olive Branch Grocer</div><div class="deal-meta">Olive Branch Grocer<br>Maple Hollow</div><div class="deal-buy"><span class="old">$40</span><span class="new">$20</span><span class="buy">Buy this deal</span></div></article>
  <article class="deal"><div class="deal-photo" role="img" aria-label="Spa face mask treatment" style="background:linear-gradient(135deg,#c99d80,#4f5b44)"></div><div class="deal-title">Half Off at Olive Branch Grocer</div><div class="deal-meta">Olive Branch Grocer<br>Maple Hollow</div><div class="deal-buy"><span class="old">$40</span><span class="new">$20</span><span class="buy">Buy this deal</span></div></article>

  <article class="deal"><div class="deal-photo" role="img" aria-label="USB memory stick" style="background:linear-gradient(135deg,#fafafa,#3a3a3a)"></div><div class="deal-title">Half Off at Olive Branch Grocer</div><div class="deal-meta">Olive Branch Grocer<br>Maple Hollow</div><div class="deal-buy"><span class="old">$40</span><span class="new">$20</span><span class="buy">Buy this deal</span></div></article>
  <article class="deal"><div class="deal-photo" role="img" aria-label="Children in hoodies" style="background:linear-gradient(90deg,#2d4e9a,#e6a6c0,#c52a2a)"></div><div class="deal-title">Half Off at Olive Branch Grocer</div><div class="deal-meta">Olive Branch Grocer<br>Maple Hollow</div><div class="deal-buy"><span class="old">$40</span><span class="new">$20</span><span class="buy">Buy this deal</span></div></article>
  <article class="deal"><div class="deal-photo" role="img" aria-label="Suede boots" style="background:linear-gradient(135deg,#e0ddd6,#6e6553)"></div><div class="deal-title">Half Off at Olive Branch Grocer</div><div class="deal-meta">Olive Branch Grocer<br>Maple Hollow</div><div class="deal-buy"><span class="old">$40</span><span class="new">$20</span><span class="buy">Buy this deal</span></div></article>
  <article class="deal"><div class="deal-photo" role="img" aria-label="Toasted sandwich" style="background:linear-gradient(135deg,#f3f3f3,#c27a3a)"></div><div class="deal-title">Half Off at Olive Branch Grocer</div><div class="deal-meta">Olive Branch Grocer<br>Maple Hollow</div><div class="deal-buy"><span class="old">$40</span><span class="new">$20</span><span class="buy">Buy this deal</span></div></article>
</section>

<div class="abs view-all">View all deals
  <svg width="13" height="11" viewBox="0 0 13 11"><path d="M1 1l4.5 4.5L1 10M7 1l4.5 4.5L7 10" fill="none" stroke="#e2f3fa" stroke-width="2.2"/></svg>
</div>

<footer class="abs footer">
  <h4>Quick Links</h4>
  <div class="links" style="left:20px">Home<br>Shop by Category<br>Latest Deals<br>Popular Deals<br>Voucher Codes<br>Advanced Search</div>
  <div class="links" style="left:114px">Get Help<br>FAQ<br>Customer Support<br>Return Policy<br>Terms of Use<br>Privacy Statement</div>
  <div class="links" style="left:208px">Gifts<br>Gift Cards<br>Mobile<br>Live off Bundlio<br>Bundlio Deals<br>Tablet POS Guide<br>Share Photos</div>
  <div class="news"><h4>Newsletter Signup</h4><p>Get newsletter for all offers and update</p><div class="field">Name :</div><div class="field">Email :</div><div class="submit">Submit</div></div>
  <div class="social">Connect to<br>our social network :<div class="icons"><i></i><i></i><i></i><i></i></div><div class="copy">Copyrights © Bright Finds Nest.<br>All rights reserved.</div></div>
</footer>

<div class="abs shade"></div>

<section class="abs modal" aria-label="Sign up for deal alerts">
  <div class="modal-head">Bright Finds Nest</div>
  <div class="steps">
    <div class="step" style="left:67px"><div class="num">01</div>Enter<br>email address</div>
    <div class="step" style="left:199px"><div class="num">02</div>Confirm<br>interest categories</div>
    <div class="step" style="left:350px"><div class="num">03</div>Click on<br>activation link</div>
  </div>
  <div class="categories" aria-label="Interest categories">
    <label class="category on"><span class="box"><svg width="7" height="6" viewBox="0 0 7 6"><path d="M1 3l2 2 3-4" fill="none" stroke="#fff" stroke-width="1.4"/></svg></span>All</label>
    <label class="category on"><span class="box"><svg width="7" height="6" viewBox="0 0 7 6"><path d="M1 3l2 2 3-4" fill="none" stroke="#fff" stroke-width="1.4"/></svg></span>Electronics</label>
    <label class="category on"><span class="box"><svg width="7" height="6" viewBox="0 0 7 6"><path d="M1 3l2 2 3-4" fill="none" stroke="#fff" stroke-width="1.4"/></svg></span>Beauty</label>
    <label class="category"><span class="box"></span>Money</label>
    <label class="category"><span class="box"></span>Fashion</label>
    <label class="category on"><span class="box"><svg width="7" height="6" viewBox="0 0 7 6"><path d="M1 3l2 2 3-4" fill="none" stroke="#fff" stroke-width="1.4"/></svg></span>Food &amp; Drink</label>
    <label class="category"><span class="box"></span>Travel</label>
    <label class="category"><span class="box"></span>Home &amp; Garden</label>
    <label class="category"><span class="box"></span>Kids &amp; Toys</label>
    <label class="category on"><span class="box"><svg width="7" height="6" viewBox="0 0 7 6"><path d="M1 3l2 2 3-4" fill="none" stroke="#fff" stroke-width="1.4"/></svg></span>Freebies</label>
    <label class="category"><span class="box"></span>Health</label>
    <label class="category"><span class="box"></span>Vouchers</label>
  </div>
  <div class="rule"></div>
  <div class="signup-form">ENTER YOUR EMAIL ID :<span class="go">GO</span></div>
  <div class="privacy">
    <svg width="18" height="24" viewBox="0 0 18 24" role="img" aria-label="Secure padlock">
      <path d="M4.5 10V7a4.5 4.5 0 0 1 9 0v3" fill="none" stroke="#8a9aa3" stroke-width="2.4"/>
      <rect x="1" y="10" width="16" height="13" rx="2" fill="#2a93bd"/>
      <circle cx="9" cy="15.5" r="1.8" fill="#fff"/>
      <rect x="8.2" y="16" width="1.6" height="4" fill="#fff"/>
    </svg>
    <div><h5>We respect your email privacy</h5><p>Your address stays safe with us behind secure SSL encryption. We never share or sell it to anyone else.</p></div>
  </div>
</section>
</body>
</html>
```